Re-branding for Structural Engineering firm

We need new business cards as part of our current re-branding. We have a new logo (attached), so the card design should incorporate this color scheme. We are a structural engineering firm providing structural building design and seismic consulting services. The final design should communicate professionalism and stability, with a modern look and feel.

```html
<!DOCTYPE html>
<html lang="en">
<head>
<meta charset="utf-8">
<title>Kelvane Structural Engineering – Business Card</title>
<link rel="stylesheet" href="https://fonts.googleapis.com/css2?family=Arimo:wght@400;700&display=swap">
<style>
  :root {
    --brand-blue: #1d6fb8;
    --brand-gray: #7d7f83;
    --text-gray: #4a4c50;
    --card-white: #ffffff;
    --page-bg: #e6e7e9;
    --rule-blue: #2a6aa8;
  }
  * { box-sizing: border-box; margin: 0; padding: 0; }
  html, body { width: 1200px; height: 997px; overflow: hidden; }
  body {
    background: var(--page-bg);
    font-family: "Arimo", Arial, sans-serif;
    position: relative;
  }
  .card {
    position: absolute;
    width: 560px;
    height: 320px;
    background: var(--card-white);
    box-shadow: 0 6px 18px rgba(0,0,0,0.18);
    overflow: hidden;
  }
  .card-back { left: 70px; top: 110px; }
  .card-front { left: 570px; top: 500px; }

  /* Back side */
  .back-brand {
    position: absolute;
    left: 0; right: 0; top: 0; bottom: 0;
    display: flex; align-items: center; justify-content: center; gap: 18px;
  }
  .brand-square { width: 62px; height: 62px; background: var(--brand-blue); }
  .back-brand .brand-name {
    color: var(--brand-blue);
    font-weight: 700;
    font-size: 30px;
    line-height: 1.05;
    letter-spacing: 0.5px;
  }

  /* Front side */
  .front-brand {
    position: absolute; right: 28px; top: 24px;
    display: flex; align-items: center; gap: 10px;
  }
  .front-brand .brand-square { width: 34px; height: 34px; }
  .front-brand .brand-name {
    color: var(--brand-blue); font-weight: 700; font-size: 15px; line-height: 1.1;
  }
  .person { position: absolute; left: 30px; top: 150px; }
  .person-name { color: var(--brand-blue); font-size: 19px; }
  .person-role { color: var(--text-gray); font-size: 12px; margin-top: 3px; }
  .name-rule {
    position: absolute; left: 160px; right: 24px; top: 162px;
    height: 1px; background: var(--rule-blue);
  }
  .contact-list { position: absolute; left: 30px; top: 205px; list-style: none; }
  .contact-list li {
    display: flex; align-items: center; gap: 10px;
    color: #222; font-size: 14px; height: 22px;
  }
  .contact-list svg { width: 14px; height: 14px; }
  .company-block {
    position: absolute; right: 28px; top: 178px; text-align: right;
  }
  .company-title { color: var(--brand-blue); font-weight: 700; font-size: 14px; }
  .company-address { color: var(--text-gray); font-size: 12px; line-height: 1.35; margin-top: 3px; }
  .bottom-bands { position: absolute; left: 0; bottom: 0; width: 560px; height: 90px; }
  .website {
    position: absolute; right: 28px; bottom: 26px;
    color: #fff; font-size: 14px;
  }
</style>
</head>
<body>

<section class="card card-back" aria-label="Card back">
  <div class="back-brand">
    <div class="brand-square"></div>
    <div class="brand-name">KELVANE<br>STRUCTURAL<br>ENGINEERING</div>
  </div>
</section>

<section class="card card-front" aria-label="Card front">
  <div class="front-brand">
    <div class="brand-square"></div>
    <div class="brand-name">KELVANE<br>STRUCTURAL<br>ENGINEERING</div>
  </div>

  <div class="name-rule"></div>
  <div class="person">
    <div class="person-name">Owen Marsh</div>
    <div class="person-role">Director</div>
  </div>

  <ul class="contact-list">
    <li>
      <svg viewBox="0 0 14 14"><circle cx="7" cy="7" r="7" fill="var(--brand-blue)"/><rect x="4" y="5" width="6" height="4" rx="1" fill="#fff"/></svg>
      (555) 214-3090
    </li>
    <li>
      <svg viewBox="0 0 14 14"><circle cx="7" cy="7" r="7" fill="var(--brand-blue)"/><rect x="4" y="4" width="6" height="6" rx="1" fill="#fff"/></svg>
      (555) 214-3091
    </li>
    <li>
      <svg viewBox="0 0 14 14"><circle cx="7" cy="7" r="7" fill="var(--brand-blue)"/><path d="M3.5 4.5h7v5h-7z M3.5 4.5l3.5 3 3.5-3" fill="none" stroke="#fff" stroke-width="1"/></svg>
      omarsh@kelvane.com
    </li>
  </ul>

  <div class="company-block">
    <div class="company-title">KELVANE STRUCTURAL ENGINEERING</div>
    <div class="company-address">418 Harbor Row, Suite 210<br>Bayport, Texas 78400</div>
  </div>

  <svg class="bottom-bands" viewBox="0 0 560 90" preserveAspectRatio="none">
    <path d="M0 68 H270 C292 68 296 44 318 40 H322 C300 46 298 74 274 74 H0 Z" fill="var(--brand-gray)"/>
    <path d="M0 82 H290 C315 82 318 36 345 30 H560 V90 H0 Z" fill="var(--brand-blue)"/>
  </svg>
  <div class="website">www.kelvanestructural.com</div>
</section>

</body>
</html>
```